TK Drafting

Simple Design - Logo is done (from this site). Logo on one side - Back Side an image or outline of a house blue print - My name, phone, email, website url. Prefer the traditional Architectural style of letters -

Target Market(s)

Customers who need a floor plan redesigned for renovations or realtors who want a floor plan for marketing their listings

Industry/Entity Type

Architecture

Contact Information for Business Card

Colby Faust - Name
415-362-8840 - Phone
tkdraftingco@mailpost.example
www.tkdraftingco.example

Font styles to use
Other font styles liked:
• Architecture writing -

Colors
0555a3
3276b5
85acd3

Requirements
Must have
• Logo that is attached. I like an indigo blue color for the background or a royal blue - gray logo OR - white and clean with the logo on one side and the same color gray lettering on the other side
Nice to have
• some sort of image that shows a residential blue print. It may not be possible on this small of a card though.
Should not have
• Nothing cartoonish.

```html
<!DOCTYPE html>
<html lang="en">
<head>
<meta charset="utf-8">
<title>TK Drafting — Business Card</title>
<link rel="stylesheet" href="https://fonts.googleapis.com/css2?family=Raleway:wght@300;400;500&display=swap">
<style>
  :root {
    --page: #e9e6ee;
    --card: #4b2a82;
    --card-deep: #42247a;
    --plan-light: #5a3a96;
    --mark-gray: #b5b3bd;
    --mark-light: #e4e2ea;
    --text-white: #f4f2f8;
  }
  * { box-sizing: border-box; margin: 0; padding: 0; }
  html, body {
    width: 1200px; height: 1023px; overflow: hidden;
    background: var(--page);
    font-family: "Raleway", sans-serif;
  }
  .canvas {
    width: 1200px; height: 1023px;
    display: flex; flex-direction: column; align-items: center; justify-content: center;
    gap: 44px;
  }
  .card {
    position: relative;
    width: 700px; height: 400px;
    background: var(--card);
    border-radius: 4px;
    overflow: hidden;
    box-shadow: 0 14px 30px rgba(40, 20, 70, 0.25);
  }

  /* Front: identity + contact */
  .brand {
    position: absolute; left: 56px; top: 120px;
    display: flex; align-items: center; gap: 16px;
  }
  .brand-square {
    width: 30px; height: 30px; background: var(--mark-gray);
  }
  .brand-name {
    font-weight: 300; font-size: 34px; letter-spacing: 8px;
    text-transform: uppercase; color: var(--mark-gray);
  }
  .contact {
    position: absolute; left: 56px; top: 206px;
    color: var(--text-white);
  }
  .contact-name {
    font-weight: 400; font-size: 25px; letter-spacing: 1.5px;
    text-transform: uppercase; margin-bottom: 16px;
  }
  .contact-line {
    display: flex; align-items: center; gap: 14px;
    font-weight: 400; font-size: 17px; line-height: 1; margin-bottom: 13px;
  }
  .contact-line svg { width: 16px; height: 16px; flex: none; }

  /* Back: plan backdrop + centered identity */
  .plan-backdrop {
    position: absolute; inset: 0;
    background: linear-gradient(115deg, var(--card-deep) 0%, var(--card) 45%, var(--plan-light) 100%);
  }
  .back-brand {
    position: absolute; inset: 0;
    display: flex; align-items: center; justify-content: center; gap: 20px;
  }
  .back-brand .brand-square { width: 40px; height: 40px; }
  .back-brand .brand-name { font-size: 44px; letter-spacing: 11px; }
</style>
</head>
<body>
<main class="canvas">

  <section class="card card-front" aria-label="Card front">
    <div class="brand">
      <span class="brand-square"></span>
      <span class="brand-name">TK Drafting</span>
    </div>
    <div class="contact">
      <p class="contact-name">Colby Faust</p>
      <p class="contact-line">
        <svg viewBox="0 0 16 16" aria-hidden="true"><circle cx="8" cy="8" r="7.5" fill="var(--mark-gray)"/><path d="M5.3 4.2l1.4 1.6-.7 1.1c.5 1.1 1.3 1.9 2.4 2.4l1.1-.7 1.6 1.4-.6 1.2c-3-.4-5.4-2.8-5.8-5.8z" fill="var(--card)"/></svg>
        415-362-8840
      </p>
      <p class="contact-line">
        <svg viewBox="0 0 16 16" aria-hidden="true"><rect x="1" y="3.5" width="14" height="9" fill="var(--mark-gray)"/><path d="M1 3.5l7 5.5 7-5.5" fill="none" stroke="var(--card)" stroke-width="1.1"/></svg>
        tkdraftingco@mailpost.example
      </p>
      <p class="contact-line">
        <svg viewBox="0 0 16 16" aria-hidden="true"><circle cx="8" cy="8" r="7" fill="var(--mark-gray)"/><g fill="none" stroke="var(--card)" stroke-width="0.9"><ellipse cx="8" cy="8" rx="3" ry="7"/><path d="M1 8h14M2.2 4.5h11.6M2.2 11.5h11.6"/></g></svg>
        www.tkdraftingco.example
      </p>
    </div>
  </section>

  <section class="card card-back" aria-label="Card back">
    <div class="plan-backdrop" role="img" aria-label="Faint residential floor plan drawing across the card"></div>
    <div class="back-brand">
      <span class="brand-square"></span>
      <span class="brand-name">TK Drafting</span>
    </div>
  </section>

</main>
</body>
</html>
```